Lidia Vanta Catering
Complete Stationery Design
Lidia Vanta Catering - Chef / Catering
Creative Brief
Bright & Fun-filled
Corazon Belmiro
Director, Sales & Marketing
2nd Floor, Quintero Bldg., Saldivar Avenue near corner Lupine Street, Navotas, Metro Manila, Philippines 1490
cbelmiro@lidiavanta-example.ph
www.lidiavanta-example.ph
Lidia Vanta is a high end catering company. Our design is modern Victorian. Color dark red, black and white but we are open to other color suggestion. We need the ff: - business cards - A4 and letter size paper with matching letter envelopes - Folder that fits A4 and letter size envelop - Fax Cover - CD sticker and cover - Sticker label - Address Sticker Label - Paper Bag Design - Styro lunch box design - Tissue Napkin Design - Name Plate - Identification Card Design
Victorian design with our Logo in the middle

```html
<!DOCTYPE html>
<html lang="en">
<head>
<meta charset="utf-8">
<title>Lidia Vanta Catering — Stationery Set</title>
<link href="https://fonts.googleapis.com/css2?family=Cormorant+Garamond:wght@500;600&family=Lato:wght@400;700&display=swap" rel="stylesheet">
<style>
  :root{
    --backdrop:#d9d6d2;
    --wine:#5e0f16;
    --wine-deep:#3b070c;
    --wine-light:#7a1a22;
    --gold:#c9a25a;
    --gold-soft:rgba(201,162,90,.35);
    --paper:#ffffff;
    --ink:#4a3a34;
    --rule:#d8cfc6;
  }
  *{box-sizing:border-box;margin:0;padding:0}
  html,body{width:1200px;height:820px;overflow:hidden;background:var(--backdrop)}
  body{position:relative;font-family:"Lato",sans-serif;color:var(--ink)}
  .piece{position:absolute;box-shadow:0 3px 10px rgba(0,0,0,.25);overflow:hidden}
  .wine{background:radial-gradient(ellipse at 50% 40%,var(--wine-light),var(--wine) 55%,var(--wine-deep));color:var(--gold)}
  .paper{background:var(--paper)}
  .brand{font-family:"Cormorant Garamond",serif;font-weight:600;color:var(--gold);white-space:nowrap;display:inline-flex;align-items:center;gap:5px}
  .brand::before{content:"";width:.45em;height:.45em;border-radius:50%;background:currentColor;display:inline-block}
  .brand.on-paper{color:var(--wine)}
  .gold-rule{position:absolute;left:0;right:0;height:2px;background:var(--gold)}
  .flourish{position:absolute;background:radial-gradient(ellipse,var(--gold-soft),transparent 70%)}
  .flourish.on-paper{background:radial-gradient(ellipse,rgba(201,162,90,.18),transparent 70%)}
  .small{font-size:6px;line-height:1.45;color:var(--gold)}
  .name{font-family:"Cormorant Garamond",serif;font-weight:600;font-size:11px;color:var(--gold)}
  .center{display:flex;flex-direction:column;align-items:center;justify-content:center;text-align:center}

  /* business cards */
  .card-front{left:89px;top:43px;width:175px;height:101px}
  .card-back{left:89px;top:163px;width:175px;height:101px}
  .card-tall{top:269px;width:106px;height:187px}
  .card-tall.a{left:53px}.card-tall.b{left:168px}

  /* letterhead & fax */
  .letterhead{left:319px;top:48px;width:204px;height:283px}
  .fax{left:533px;top:48px;width:211px;height:283px}
  .sheet-foot{position:absolute;left:0;right:0;bottom:0;height:16px;background:var(--wine);font-size:5px;color:var(--gold);display:flex;align-items:center;justify-content:center}
  .fax-title{position:absolute;right:14px;top:14px;font-weight:700;font-size:10px;color:var(--wine)}
  .fax-form{position:absolute;left:14px;right:14px;top:44px;display:grid;grid-template-columns:1fr 1fr;gap:7px 12px;font-size:5.5px}
  .fax-form span{border-bottom:1px solid var(--rule);padding-bottom:2px}
  .fax-checks{position:absolute;left:14px;right:14px;top:122px;display:flex;justify-content:space-between;font-size:5.5px;line-height:8px}
  .fax-checks span::before{content:"";display:inline-block;width:5px;height:5px;border:1px solid var(--wine);margin-right:3px;vertical-align:-1px}
  .fax-lines{position:absolute;left:14px;right:14px;top:140px;height:1px;background:var(--rule)}

  /* envelopes */
  .env-window{left:293px;top:336px;width:211px;height:120px}
  .env-plain{left:533px;top:336px;width:211px;height:120px}
  .env-back{left:329px;top:468px;width:211px;height:96px}
  .env-flap{position:absolute;inset:0;width:100%;height:100%}
  .env-brand{position:absolute;left:0;right:0;top:54px}
  .window{position:absolute;left:22px;top:78px;width:62px;height:18px;background:var(--paper);border-radius:2px}
  .return-address{position:absolute;right:10px;bottom:9px;font-size:5px;text-align:right}

  /* folder */
  .folder{left:763px;top:48px;width:384px;height:348px;background:none;box-shadow:none;overflow:visible}
  .folder-panel{position:absolute;left:0;top:0;width:384px;height:210px;box-shadow:0 3px 10px rgba(0,0,0,.25)}
  .folder-pocket{position:absolute;left:0;top:214px;width:384px;height:134px}
  .pocket-card{position:absolute;left:262px;top:260px;width:76px;height:42px;border:1px solid var(--gold);display:flex;align-items:center;justify-content:center}

  /* discs */
  .disc{position:absolute;border-radius:50%;box-shadow:0 3px 10px rgba(0,0,0,.3)}
  .disc-white{left:48px;top:480px;width:206px;height:206px;background:var(--paper)}
  .disc-wine{left:192px;top:571px;width:216px;height:216px}
  .hub{position:absolute;left:50%;top:50%;width:54px;height:54px;margin:-27px 0 0 -27px;border-radius:50%;background:#eeeae6;border:8px solid #dcd6d0}
  .hub::after{content:"";position:absolute;left:50%;top:50%;width:14px;height:14px;margin:-7px 0 0 -7px;border-radius:50%;background:var(--backdrop)}

  /* cd cover */
  .cd-cover{left:648px;top:468px;width:420px;height:300px;display:flex;gap:3px;background:none;box-shadow:none}
  .cd-panel{position:relative;flex:1;box-shadow:0 3px 10px rgba(0,0,0,.25)}
</style>
</head>
<body>

<!-- business card front -->
<div class="piece wine card-front center">
  <div class="gold-rule" style="top:8px"></div>
  <div class="gold-rule" style="bottom:8px"></div>
  <div class="flourish" role="img" aria-label="Victorian scroll ornament" style="left:0;top:10px;width:80px;height:80px"></div>
  <span class="brand" style="font-size:17px">Lidia Vanta</span>
</div>

<!-- business card back -->
<div class="piece wine card-back">
  <div class="flourish" role="img" aria-label="Victorian scroll ornament" style="right:0;top:0;width:90px;height:60px"></div>
  <div style="position:absolute;left:12px;top:12px">
    <div class="name">Corazon Belmiro</div>
    <div class="small">Director, Sales &amp; Marketing</div>
  </div>
  <div class="small" style="position:absolute;left:12px;top:46px;width:95px">
    +63 2 8555 0142<br>cbelmiro@lidiavanta-example.ph<br>www.lidiavanta-example.ph
  </div>
  <span class="brand" style="position:absolute;right:10px;bottom:12px;font-size:11px">Lidia Vanta</span>
</div>

<!-- tall cards -->
<div class="piece wine card-tall a">
  <div class="gold-rule" style="top:6px"></div>
  <div class="flourish" role="img" aria-label="Victorian scroll ornament" style="left:0;top:10px;width:106px;height:60px"></div>
  <div class="center" style="position:absolute;left:0;right:0;top:30px"><span class="brand" style="font-size:13px">Lidia Vanta</span></div>
  <div class="center" style="position:absolute;left:0;right:0;top:80px">
    <div class="name" style="font-size:9px">Corazon Belmiro</div>
    <div class="small">Director, Sales &amp; Marketing</div>
  </div>
  <div class="gold-rule" style="bottom:6px"></div>
</div>
<div class="piece wine card-tall b">
  <div class="flourish" role="img" aria-label="Victorian scroll ornament" style="left:0;bottom:0;width:106px;height:70px"></div>
  <div class="center" style="position:absolute;left:0;right:0;top:24px"><span class="brand" style="font-size:13px">Lidia Vanta</span></div>
  <div class="small" style="position:absolute;left:8px;right:8px;top:80px;text-align:center;font-size:5px">
    2nd Floor, Quintero Bldg., Saldivar Avenue near corner Lupine Street, Navotas, Metro Manila, Philippines 1490<br>+63 2 8555 0142<br>www.lidiavanta-example.ph
  </div>
</div>

<!-- letterhead -->
<div class="piece paper letterhead">
  <div class="center" style="position:absolute;left:0;right:0;top:14px"><span class="brand on-paper" style="font-size:14px">Lidia Vanta</span></div>
  <div class="flourish on-paper" role="img" aria-label="Faint Victorian scroll ornament" style="right:0;bottom:16px;width:120px;height:110px"></div>
  <div class="sheet-foot">2nd Floor, Quintero Bldg., Saldivar Avenue, Navotas · +63 2 8555 0142</div>
</div>

<!-- fax cover -->
<div class="piece paper fax">
  <span class="brand on-paper" style="position:absolute;left:14px;top:12px;font-size:13px">Lidia Vanta</span>
  <div class="fax-title">FAX</div>
  <div class="fax-form">
    <span>To:</span><span>From:</span>
    <span>Fax:</span><span>Pages:</span>
    <span>Phone:</span><span>Date:</span>
    <span>Re:</span><span>&nbsp;</span>
  </div>
  <div class="fax-checks"><span>Urgent</span><span>For Review</span><span>Please Reply</span></div>
  <div class="fax-lines"></div>
  <div class="flourish on-paper" role="img" aria-label="Faint Victorian scroll ornament" style="right:0;bottom:16px;width:120px;height:110px"></div>
  <div class="sheet-foot">2nd Floor, Quintero Bldg., Saldivar Avenue, Navotas · +63 2 8555 0142</div>
</div>

<!-- envelopes -->
<div class="piece wine env-window">
  <svg class="env-flap" viewBox="0 0 211 120" preserveAspectRatio="none"><polyline points="0,2 105,40 211,2" fill="none" stroke="#c9a25a" stroke-width="1.5"/></svg>
  <div class="center env-brand"><span class="brand" style="font-size:12px">Lidia Vanta</span></div>
  <div class="window"></div>
  <div class="small return-address">Lidia Vanta Catering<br>Navotas, Metro Manila</div>
</div>
<div class="piece wine env-plain">
  <svg class="env-flap" viewBox="0 0 211 120" preserveAspectRatio="none"><polyline points="0,2 105,40 211,2" fill="none" stroke="#c9a25a" stroke-width="1.5"/></svg>
  <div class="flourish" role="img" aria-label="Victorian scroll ornament" style="right:0;bottom:0;width:90px;height:60px"></div>
  <div class="center env-brand"><span class="brand" style="font-size:12px">Lidia Vanta</span></div>
</div>
<div class="piece wine env-back">
  <svg class="env-flap" viewBox="0 0 211 96" preserveAspectRatio="none"><polygon points="0,0 105,52 211,0" fill="#4a0a10" stroke="#c9a25a" stroke-width="1.5"/></svg>
</div>

<!-- presentation folder -->
<div class="piece folder">
  <div class="folder-panel wine">
    <div class="gold-rule" style="bottom:10px"></div>
    <div class="flourish" role="img" aria-label="Victorian scroll ornament" style="right:0;top:0;width:200px;height:200px"></div>
    <div class="small" style="position:absolute;left:24px;top:70px;width:130px">
      Lidia Vanta Catering<br>2nd Floor, Quintero Bldg., Saldivar Avenue near corner Lupine Street, Navotas, Metro Manila, Philippines 1490<br>+63 2 8555 0142<br>www.lidiavanta-example.ph
    </div>
    <span class="brand" style="position:absolute;right:36px;top:62px;font-size:20px">Lidia Vanta</span>
  </div>
  <svg class="folder-pocket" viewBox="0 0 384 134" preserveAspectRatio="none" aria-hidden="true">
    <defs><linearGradient id="pocketTone" x1="0" y1="0" x2="0" y2="1"><stop offset="0" stop-color="#6a141b"/><stop offset="1" stop-color="#3b070c"/></linearGradient></defs>
    <path d="M0,0 H165 L178,30 L190,0 H384 V134 H0 Z" fill="url(#pocketTone)"/>
    <line x1="0" y1="4" x2="165" y2="4" stroke="#c9a25a" stroke-width="1.5"/>
    <line x1="190" y1="4" x2="384" y2="4" stroke="#c9a25a" stroke-width="1.5"/>
  </svg>
  <div class="pocket-card wine"><span class="brand" style="font-size:9px">Lidia Vanta</span></div>
</div>

<!-- discs -->
<div class="disc disc-white">
  <div class="center" style="position:absolute;left:0;right:0;top:28px"><span class="brand on-paper" style="font-size:14px">Lidia Vanta</span></div>
  <div class="hub"></div>
  <div style="position:absolute;left:0;right:0;bottom:38px;text-align:center;font-size:6px;color:var(--wine)">www.lidiavanta-example.ph</div>
</div>
<div class="disc disc-wine wine">
  <div class="flourish" role="img" aria-label="Victorian scroll ornament" style="left:20px;top:20px;width:176px;height:80px"></div>
  <div class="hub"></div>
  <div class="small" style="position:absolute;left:0;right:0;bottom:36px;text-align:center">www.lidiavanta-example.ph</div>
</div>

<!-- cd cover -->
<div class="piece cd-cover">
  <div class="cd-panel wine">
    <div class="gold-rule" style="top:60px;height:1px"></div>
    <div class="gold-rule" style="bottom:60px;height:1px"></div>
    <div class="flourish" role="img" aria-label="Victorian scroll ornament" style="left:0;top:0;width:208px;height:140px"></div>
    <div class="center" style="position:absolute;left:0;right:0;top:24px"><span class="brand" style="font-size:13px">Lidia Vanta</span></div>
  </div>
  <div class="cd-panel wine">
    <div class="gold-rule" style="top:60px;height:1px"></div>
    <div class="gold-rule" style="bottom:60px;height:1px"></div>
    <div class="flourish" role="img" aria-label="Victorian scroll ornament" style="left:0;bottom:0;width:208px;height:140px"></div>
    <div class="center" style="position:absolute;left:0;right:0;top:22px"><span class="brand" style="font-size:16px">Lidia Vanta</span></div>
    <div class="small" style="position:absolute;left:30px;right:30px;top:110px;text-align:center">
      2nd Floor, Quintero Bldg., Saldivar Avenue near corner Lupine Street, Navotas, Metro Manila, Philippines 1490<br>www.lidiavanta-example.ph
    </div>
  </div>
</div>

</body>
</html>
```